National online rug retailer needs a home page design

See the LoomNest logo and create a home page design around that color theme. Details are spelled out in word document uploaded below.
Updates

Apparently this website did not take my attachement showing the logo and basic requirements.  If you would send me your email address, I will send you the attachment directly.
Best regards,
Ned Carver
ncarver@qwplex.com

Target Market(s)

The target market is home owners 25 to 75 years old with combined incomes over $100,000 per year.

Industry/Entity Type

Online

Requirements
Must have
• Lots of white space with black letters and creative use of red and possibly one other color. Would like a compelling call to action button.

```html
<!DOCTYPE html>
<html lang="en">
<head>
<meta charset="utf-8">
<title>LoomNest — Home</title>
<link href="https://fonts.googleapis.com/css2?family=Arimo:wght@400;700&family=Questrial&family=Cutive+Mono&family=Crimson+Text&display=swap" rel="stylesheet">
<style>
:root{
  --red:#d6141b;
  --ink:#111111;
  --grey:#5c5c5c;
  --line:#333333;
  --soft:#e6e6e6;
  --white:#ffffff;
}
*{margin:0;padding:0;box-sizing:border-box}
html,body{width:811px;height:1200px;overflow:hidden;background:var(--white)}
.page{position:relative;width:811px;height:1200px;font-family:'Arimo',Arial,sans-serif;color:var(--ink)}
.abs{position:absolute}
.top-bar{left:0;top:0;width:811px;height:5px;background:var(--red)}
.header{left:0;top:5px;width:811px;height:86px;border-bottom:1px solid #ddd;box-shadow:0 2px 3px rgba(0,0,0,.08)}
.brand{left:128px;top:38px;font-family:'Questrial',sans-serif;font-size:24px;color:var(--red);letter-spacing:.3px}
.brand-tag{left:176px;top:69px;font-size:6.5px;color:var(--grey);font-family:'Arimo',sans-serif}
.nav-item{top:46px;font-family:'Questrial',sans-serif;font-size:16px;color:#666;transform:translateX(-50%);white-space:nowrap}
.nav-item.active{color:var(--red)}
.nav-divider{top:5px;width:1px;height:85px;background:#e3e3e3}
.nav-underline{left:392px;top:85px;width:60px;height:5px;background:var(--red)}
.rule{height:1px;background:var(--line)}
.drop{width:14px;height:24px}
.center{transform:translateX(-50%);white-space:nowrap;text-align:center}
.section-title{font-weight:700;font-size:24px}
.section-title.red{color:var(--red)}
.subtitle{font-family:'Cutive Mono',monospace;font-size:11px;letter-spacing:9px}
.hero-frame{left:90px;top:225px;width:631px;height:332px;background:var(--white);box-shadow:0 0 4px rgba(0,0,0,.2)}
.hero-image{left:94px;top:229px;width:623px;height:326px;background:linear-gradient(135deg,#2a1712 0%,#b51d16 35%,#c9a34a 55%,#b51d16 75%,#1e1a2a 100%)}
.hero-shadow{left:104px;top:557px;width:610px;height:36px;background:radial-gradient(ellipse at 50% 0%,rgba(0,0,0,.35),rgba(0,0,0,0) 70%)}
.feature-icon{width:62px;height:62px;border-radius:50%;background:radial-gradient(circle at 45% 35%,#6a6a6a,#2a2a2a 75%);box-shadow:0 3px 6px rgba(0,0,0,.35)}
.feature-title{top:775px;font-weight:700;font-size:15px}
.feature-text{top:803px;width:200px;font-family:'Questrial',sans-serif;font-size:16px;line-height:18px;color:var(--grey)}
.bracket{width:21px;height:21px}
.bracket.tl{border-top:2px solid var(--red);border-left:2px solid var(--red)}
.bracket.br{border-bottom:2px solid var(--ink);border-right:2px solid var(--ink)}
.serif-head{font-family:'Crimson Text',serif;color:var(--red);letter-spacing:.8px}
.quote{left:242px;top:1030px;width:210px;font-size:8.5px;line-height:11px;color:#333}
.small-link{font-family:'Crimson Text',serif;font-size:9px;letter-spacing:.5px;color:#333}
.product-image{left:137px;top:1026px;width:93px;height:70px;background:linear-gradient(160deg,#f4f4f4 10%,#3f7a76 45%,#2f5f5c 70%,#f2f2f2 95%)}
.news-image{left:503px;top:1018px;width:67px;height:70px;background:linear-gradient(160deg,#7c6a55,#b33a2c 55%,#2e3a5c)}
.vdivider{left:466px;top:990px;width:1px;height:124px;background:#cccccc}
.footer-links{left:392px;top:1156px;font-size:8px;color:#666;word-spacing:12px}
.copyright{left:392px;top:1178px;font-size:6.5px;letter-spacing:1px}
</style>
</head>
<body>
<div class="page">
  <div class="abs top-bar"></div>
  <header class="abs header"></header>
  <div class="abs brand">LoomNest.com</div>
  <div class="abs brand-tag">for domestic and heirloom values</div>

  <nav>
    <span class="abs nav-item active" style="left:423px">HOME</span>
    <span class="abs nav-divider" style="left:470px"></span>
    <span class="abs nav-item" style="left:510px">OFFERS</span>
    <span class="abs nav-divider" style="left:554px"></span>
    <span class="abs nav-item" style="left:607px">CONTACT US</span>
    <span class="abs nav-divider" style="left:659px"></span>
    <span class="abs nav-item" style="left:697px">MENU</span>
    <span class="abs nav-underline"></span>
  </nav>

  <!-- Best collections -->
  <div class="abs rule" style="left:271px;top:151px;width:98px"></div>
  <div class="abs rule" style="left:397px;top:151px;width:105px"></div>
  <svg class="abs drop" style="left:379px;top:137px" viewBox="0 0 14 24"><path d="M9 1 C3 2 1 8 3 12 C4 15 4 19 2 23 C7 19 12 13 12 7 C12 4 11 2 9 1 Z" fill="var(--red)"/></svg>
  <div class="abs section-title center" style="left:392px;top:167px">BEST COLLECTIONS</div>
  <div class="abs subtitle center" style="left:396px;top:197px">you can find ever</div>

  <div class="abs hero-frame"></div>
  <div class="abs hero-image" role="img" aria-label="Close-up of an embroidered rug with red, gold and blue floral motifs"></div>
  <div class="abs hero-shadow"></div>

  <!-- Unlimited designs -->
  <div class="abs rule" style="left:271px;top:603px;width:98px"></div>
  <div class="abs rule" style="left:397px;top:603px;width:105px"></div>
  <svg class="abs drop" style="left:379px;top:589px" viewBox="0 0 14 24"><path d="M9 1 C3 2 1 8 3 12 C4 15 4 19 2 23 C7 19 12 13 12 7 C12 4 11 2 9 1 Z" fill="var(--ink)"/></svg>
  <div class="abs section-title red center" style="left:398px;top:620px">UNLIMATED DESIGNS</div>

  <div class="abs feature-icon" style="left:142px;top:690px">
    <svg width="62" height="62" viewBox="0 0 62 62"><circle cx="31" cy="22" r="7" fill="#eee"/><path d="M19 46 C19 34 24 30 31 30 C38 30 43 34 43 46 Z" fill="#eee"/></svg>
  </div>
  <div class="abs feature-icon" style="left:367px;top:690px">
    <svg width="62" height="62" viewBox="0 0 62 62"><path d="M31 16 C24 16 21 21 21 26 C21 31 26 33 26 38 L36 38 C36 33 41 31 41 26 C41 21 38 16 31 16 Z" fill="none" stroke="#eee" stroke-width="2.5"/><rect x="26" y="40" width="10" height="3" fill="#eee"/><rect x="27" y="44" width="8" height="3" fill="#eee"/></svg>
  </div>
  <div class="abs feature-icon" style="left:589px;top:690px">
    <svg width="62" height="62" viewBox="0 0 62 62"><path d="M17 33 L46 23 L34 38 Z" fill="#eee"/><path d="M17 33 L46 23 L30 35 Z" fill="#bbb"/></svg>
  </div>

  <div class="abs feature-title center" style="left:177px">OLD FASHOINS</div>
  <div class="abs feature-title center" style="left:415px">BRIGHTNESS IDEA</div>
  <div class="abs feature-title center" style="left:621px">WE DELEVERE</div>
  <p class="abs feature-text" style="left:95px">Dummy data is benign in-formation that .</p>
  <p class="abs feature-text" style="left:320px">Dummy data is benign in-formation that .</p>
  <p class="abs feature-text" style="left:542px">Dummy data is benign in-formation that .</p>

  <!-- After selling service -->
  <div class="abs rule" style="left:271px;top:882px;width:98px"></div>
  <div class="abs rule" style="left:397px;top:882px;width:105px"></div>
  <svg class="abs drop" style="left:379px;top:868px" viewBox="0 0 14 24"><path d="M9 1 C3 2 1 8 3 12 C4 15 4 19 2 23 C7 19 12 13 12 7 C12 4 11 2 9 1 Z" fill="var(--ink)"/></svg>
  <div class="abs section-title red center" style="left:392px;top:900px">AFTER SELLING SERVECE</div>
  <div class="abs center" style="left:385px;top:933px;font-weight:700;font-size:15px">ABOUT OUR SERVICES</div>

  <div class="abs bracket tl" style="left:137px;top:993px"></div>
  <div class="abs product-image" role="img" aria-label="Rolled teal rug with a leaf border"></div>
  <div class="abs bracket br" style="left:212px;top:1097px"></div>
  <div class="abs serif-head" style="left:242px;top:996px;font-size:13px">HOW CAN YOU CHANGE</div>
  <p class="abs quote">"We go to extraordinary lengths to provide world-class healthcare staffing and believe we can help achieve real improvements in patient care."</p>
  <div class="abs small-link" style="left:378px;top:1083px">WATCH DEMO</div>

  <div class="abs vdivider"></div>

  <div class="abs bracket tl" style="left:488px;top:1009px"></div>
  <div class="abs news-image" role="img" aria-label="Rug merchant standing beside hanging carpets"></div>
  <div class="abs bracket br" style="left:568px;top:1078px"></div>
  <div class="abs serif-head" style="left:590px;top:1002px;font-size:11px">NEWS</div>
  <p class="abs" style="left:593px;top:1030px;width:80px;font-size:8px;line-height:11px;color:#333">What's going on in our world</p>
  <div class="abs" style="left:628px;top:1064px;font-size:30px;color:var(--red)">?</div>

  <!-- Footer -->
  <div class="abs rule" style="left:271px;top:1144px;width:233px"></div>
  <div class="abs footer-links center">HOME ABOUT&nbsp;US DESIGNS CONTACT&nbsp;US</div>
  <div class="abs copyright center">ALL COPYRIGHTS RESEVED BY RUG COMPANY</div>
  <div class="abs" style="left:271px;top:1193px;width:233px;height:1px;background:var(--red)"></div>
</div>
</body>
</html>
```